Talbrin Business Cards

Front and back. Simon Kavelle MBA is the CEO of Talbrin Homes. Black white and grays. Logo and cool design.

Target Market(s)

Professional lenders and investors

Industry/Entity Type

Real estate developer. NO HOUSES OR ROOFS

Contact Information for Business Card

Logo, name and unique design. Front and back. Simon Kavelle MBA is the CEO of Talbrin Homes. Black white and grays. Logo and cool design.

Font styles to use
Sans Serif

Colors

Designer to choose only greyscale colors for use in the design.

Requirements
Must have
• Cool look. Not the same card I could design.
Nice to have
• Something memorable
Should not have
• Basic

```html
<!DOCTYPE html>
<html lang="en">
<head>
<meta charset="utf-8">
<title>Talbrin Homes – Business Cards</title>
<link href="https://fonts.googleapis.com/css2?family=Poppins:wght@400;600;700&display=swap" rel="stylesheet">
<style>
  :root {
    --stage: #1c1c1c;
    --ink: #111111;
    --paper: #ffffff;
    --front-mark: #3a3a3a;
    --muted: #222222;
  }
  * { margin: 0; padding: 0; box-sizing: border-box; }
  html, body { width: 1200px; height: 1015px; overflow: hidden; }
  body {
    background: var(--stage);
    font-family: "Poppins", sans-serif;
    display: flex;
    flex-direction: column;
    align-items: center;
    justify-content: center;
    gap: 50px;
  }
  .card {
    position: relative;
    width: 760px;
    height: 434px;
    overflow: hidden;
  }
  .card-front {
    background: var(--ink);
    display: flex;
    align-items: center;
    justify-content: center;
  }
  .wordmark {
    font-weight: 700;
    letter-spacing: -1px;
    line-height: 1;
    white-space: nowrap;
  }
  .card-front .wordmark { font-size: 66px; color: var(--front-mark); }

  .card-back { background: var(--paper); }
  .card-back .wave { position: absolute; inset: 0; }
  .card-back .wordmark {
    position: absolute;
    left: 50px;
    top: 138px;
    font-size: 44px;
    color: var(--ink);
  }
  .holder {
    position: absolute;
    right: 60px;
    top: 40px;
    text-align: right;
    color: var(--muted);
  }
  .holder-name { font-size: 22px; font-weight: 600; line-height: 1.2; }
  .holder-role { font-size: 16px; font-weight: 400; line-height: 1.3; }

  .contact {
    position: absolute;
    right: 34px;
    top: 200px;
    list-style: none;
    color: var(--paper);
    text-align: right;
    font-size: 17px;
    line-height: 1.5;
  }
  .contact li { display: flex; align-items: center; justify-content: flex-end; gap: 10px; }
  .contact .address { margin-top: 6px; line-height: 1.35; }
  .contact svg { width: 16px; height: 16px; flex: none; }
  .contact .no-icon { padding-right: 26px; }
</style>
</head>
<body>
  <section class="card card-front">
    <span class="wordmark">Talbrin Homes</span>
  </section>

  <section class="card card-back">
    <svg class="wave" viewBox="0 0 760 434" preserveAspectRatio="none">
      <path d="M0,320 C220,342 330,302 440,212 C540,132 640,120 760,120" fill="none" stroke="#111" stroke-width="8"/>
      <path d="M0,338 C220,360 330,320 440,230 C540,150 640,138 760,138" fill="none" stroke="#111" stroke-width="6"/>
      <path d="M0,356 C220,378 330,338 440,246 C540,166 640,154 760,154 L760,434 L0,434 Z" fill="#111"/>
    </svg>

    <span class="wordmark">Talbrin Homes</span>

    <div class="holder">
      <p class="holder-name">Owen Marlow</p>
      <p class="holder-role">Managing Director</p>
    </div>

    <ul class="contact">
      <li>044-123 456 789
        <svg viewBox="0 0 24 24"><path fill="#fff" d="M6.6 10.8a15 15 0 006.6 6.6l2.2-2.2a1 1 0 011-.25 11.4 11.4 0 003.6.57 1 1 0 011 1V20a1 1 0 01-1 1A17 17 0 013 4a1 1 0 011-1h3.5a1 1 0 011 1c0 1.25.2 2.45.57 3.6a1 1 0 01-.25 1z"/></svg>
      </li>
      <li>info@webname.com
        <svg viewBox="0 0 24 24"><path fill="#fff" d="M2 5h20v14H2z"/><path d="M2 5l10 8 10-8" fill="none" stroke="#111" stroke-width="1.6"/></svg>
      </li>
      <li>www.websitename.com
        <svg viewBox="0 0 24 24"><circle cx="12" cy="12" r="10" fill="#fff"/><path d="M2 12h20M12 2c3 3 3 17 0 20M12 2c-3 3-3 17 0 20" fill="none" stroke="#111" stroke-width="1.2"/></svg>
      </li>
      <li class="address">421, Address line here
        <svg viewBox="0 0 24 24"><path fill="#fff" d="M12 2a7 7 0 017 7c0 5-7 13-7 13S5 14 5 9a7 7 0 017-7z"/><circle cx="12" cy="9" r="2.6" fill="#111"/></svg>
      </li>
      <li class="no-icon">Country Name, 45452</li>
    </ul>
  </section>
</body>
</html>
```